Business card design needed

New company based in Brisbane, Australia. Brindle Technologies. The business is focused on the delivery of network architecture design and deployment. We will provide both services and the sale of the necessary equipment to deliver the service. Cloud computing is an important element of our focus as this is an emerging market for enterprises in Queensland. Our target marketplace is medium to large corporations with complex infrastructure requirements. IT Management and above will be the typical entry point for us into these accounts. We would like to see the use of various shade of green, design should be clutter free and impress stability, trust and growth.
Updates
Hey Everyone
Just we let you all know we have changed this project to 'committed' payment status.
Looking forward to seeing the designs! Thanks for your efforts.
Best Regards
Martin
Industry/Entity Type
Architecture
Contact Information for Business Card
Brindle Technologies, Martin Coulter, Sales Director, Level 19 Harwell Court, 58 Kelvane Street, Brisbane QLD 4000, Ph +61 7 3946 2271, M +61 4 4208 6157, E martin.coulter@brindletechnologies-example.com.au
Look and feel
Each slider illustrates characteristics of the customer's brand and the style your logo design should communicate.

```html
<!DOCTYPE html>
<html lang="en">
<head>
<meta charset="utf-8">
<title>Martin Coulter — Brindle Technologies</title>
<link rel="stylesheet" href="https://fonts.googleapis.com/css2?family=Open+Sans:wght@400&family=Poiret+One&display=swap">
<style>
  :root {
    --leaf-green: #8dc63f;
    --leaf-green-soft: rgba(141, 198, 63, 0.28);
    --leaf-green-fade: rgba(141, 198, 63, 0);
    --slate-grey: #58595b;
    --ink: #3c3c3c;
    --paper: #ffffff;
  }
  html, body {
    margin: 0;
    padding: 0;
    width: 1200px;
    height: 589px;
    overflow: hidden;
    background: var(--paper);
  }
  .business-card {
    position: relative;
    width: 1200px;
    height: 589px;
    background: var(--paper);
    overflow: hidden;
  }
  .header-flourish {
    position: absolute;
    left: 0;
    top: 0;
    width: 1200px;
    height: 175px;
    background: linear-gradient(175deg, var(--leaf-green-fade) 10%, var(--leaf-green-soft) 55%, var(--leaf-green-fade) 100%);
  }
  .holder-name {
    position: absolute;
    left: 68px;
    top: 190px;
    margin: 0;
    font-family: "Open Sans", sans-serif;
    font-weight: 400;
    font-size: 62px;
    line-height: 1;
    letter-spacing: -0.5px;
    color: var(--slate-grey);
  }
  .holder-name .first-name {
    color: var(--leaf-green);
  }
  .holder-title {
    position: absolute;
    left: 70px;
    top: 287px;
    margin: 0;
    font-family: "Poiret One", sans-serif;
    font-size: 25px;
    line-height: 1;
    letter-spacing: 23.5px;
    word-spacing: 32px;
    color: var(--ink);
  }
  .contact-details {
    position: absolute;
    left: 56px;
    top: 444px;
    margin: 0;
    font-family: "Poiret One", sans-serif;
    font-style: normal;
    font-size: 25px;
    line-height: 34px;
    color: var(--ink);
  }
  .contact-details span {
    display: block;
    white-space: nowrap;
  }
</style>
</head>
<body>
<main class="business-card">
  <div class="header-flourish" role="img" aria-label="Decorative band of sweeping green lines across the top of the card"></div>

  <h1 class="holder-name"><span class="first-name">Martin</span> Coulter</h1>
  <p class="holder-title">Sales Director</p>

  <address class="contact-details">
    <span class="street-address">Level 19 Harwell Court 58 Kelvane Street. Brisbane QLD 4000</span>
    <span class="phone">Ph : + 61 7 3946 2271</span>
    <span class="mobile">M : + 61 4 4208 6157</span>
    <span class="email">E : martin.coulter@brindletechnologies-example.com.au</span>
  </address>
</main>
</body>
</html>
```